Redesign of codeharborworks.net including blog.

We now have a design in layered PSD files. The design is almost there but needs some tweaking and some great coding to get it in place!

We no longer need SEO help, just brilliant coding and some design tweaks.

Please feel free to ask me any questions.

Please note:
1. This is my first time using artflockly, and as such, am not yet ready to make this a guaranteed project. I'm sure I'll be able to do that on subsequent projects when I gain more trust in the process.
2. My clients are always looking for good designers. Always. What I'm doing here is testing the process for myself. If I'm happy with your design and your work ethic, be sure that I'll be sending more work your way.

Thanks for your interest in the project.

Hello Designers! The project is now GUARANTEED!

Industry/Entity Type

Seo

Requirements
Must have
• * Same idea of having image sliders on the homepage
* Must be smartphone compatible
* High resolution images and icons supporting retina display

```html
<!DOCTYPE html>
<html lang="en">
<head>
<meta charset="utf-8">
<title>CodeHarborWorks – Home</title>
<link rel="stylesheet" href="https://fonts.googleapis.com/css2?family=Jost:wght@400;500;700&family=Roboto+Condensed:wght@700&family=Arimo&display=swap">
<style>
  :root {
    --accent: #d05a5a;
    --accent-dark: #b84444;
    --ink: #444446;
    --ink-soft: #555;
    --link-blue: #4a7fb5;
    --header-bg: #ececec;
    --hero-bg: #e8e8e8;
    --page-bg: #ffffff;
    --footer-bg: #333335;
    --footer-text: #a9a9a9;
    --rule: #c9c9c9;
  }
  * { box-sizing: border-box; margin: 0; padding: 0; }
  html, body { width: 1200px; height: 785px; overflow: hidden; background: var(--page-bg); }
  body { position: relative; font-family: "Jost", sans-serif; color: var(--ink); }

  .site-header { position: absolute; left: 0; top: 0; width: 1200px; height: 117px; background: var(--header-bg); border-bottom: 3px solid var(--accent); }
  .brand { position: absolute; left: 184px; top: 89px; font-size: 14px; line-height: 16px; color: var(--ink); letter-spacing: 0.2px; white-space: nowrap; }

  .search { position: absolute; left: 841px; top: 19px; width: 185px; height: 25px; background: #f7f7f7; border: 1px solid #bdbdbd; }
  .search-label { position: absolute; left: 10px; top: 4px; font-family: "Arimo", sans-serif; font-size: 12px; color: #999; }
  .search-icon { position: absolute; right: 0; top: 0; width: 34px; height: 23px; border-left: 1px solid #cfcfcf; }

  .main-nav { position: absolute; left: 347px; top: 86px; display: flex; font-size: 16px; }
  .main-nav a { color: var(--ink); text-decoration: none; padding: 0 9px; border-left: 1px solid var(--rule); line-height: 18px; position: relative; }
  .main-nav a:first-child { border-left: none; }
  .main-nav a.is-current { color: var(--accent); }
  .main-nav a.is-current::after { content: ""; position: absolute; left: 50%; margin-left: -6px; top: 25px; border: 6px solid transparent; border-bottom-color: var(--accent); border-top: 0; }

  .hero { position: absolute; left: 0; top: 117px; width: 1200px; height: 298px; background: var(--hero-bg); }
  .hero-title { position: absolute; left: 201px; top: 60px; font-size: 31px; font-weight: 700; color: var(--ink); letter-spacing: 0.5px; }
  .hero-title .code-word { color: var(--accent); }
  .hero-line { position: absolute; left: 201px; font-size: 20px; color: var(--ink); }
  .hero-line.one { top: 98px; }
  .hero-line.two { top: 132px; }
  .hero-cta-word { position: absolute; left: 201px; top: 170px; font-size: 29px; font-weight: 700; color: var(--accent); }
  .hero-button { position: absolute; left: 198px; top: 218px; width: 288px; height: 33px; border-radius: 17px; background: linear-gradient(#dc6a6a, var(--accent-dark)); box-shadow: 0 1px 2px rgba(0,0,0,.3); color: #fff; font-family: "Arimo", sans-serif; font-weight: 700; font-size: 15px; line-height: 33px; padding-left: 17px; }
  .hero-button svg { position: absolute; right: 16px; top: 9px; }
  .hero-art { position: absolute; left: 683px; top: 8px; width: 268px; height: 281px; border-radius: 6px; background: linear-gradient(160deg, #d9d9d9, #cdd5df 55%, #d8c8c4); }
  .slider-dots { position: absolute; left: 563px; top: 275px; display: flex; gap: 7px; }
  .slider-dots span { width: 15px; height: 15px; border-radius: 50%; background: #dcdcdc; box-shadow: inset 0 1px 2px rgba(0,0,0,.25); }

  .welcome { position: absolute; left: 166px; top: 432px; width: 850px; }
  .welcome h1 { font-size: 22px; font-weight: 400; color: var(--ink-soft); margin-bottom: 11px; }
  .welcome p { font-size: 13px; line-height: 16px; color: var(--ink-soft); margin-bottom: 15px; }
  .welcome h1 span { color: var(--link-blue); }

  .services { position: absolute; left: 166px; top: 582px; display: flex; gap: 16px; }
  .service { width: 161px; text-align: center; }
  .service-thumb { width: 161px; height: 81px; border: 1px solid #a8a8a8; }
  .service-label { margin-top: 5px; font-family: "Roboto Condensed", sans-serif; font-weight: 700; font-size: 15px; color: #6a6a6a; }
  .service-label b { color: var(--accent); }
  .thumb-web { background: linear-gradient(#e6e6e6, #9aa0a6); }
  .thumb-social { background: linear-gradient(135deg, #c85b4a, #8e87c9 50%, #c9a85a); }
  .thumb-server { background: linear-gradient(90deg, #2f2f33, #eaeaea 50%, #2f2f33); }
  .thumb-cloud { background: linear-gradient(#ffffff, #b9d6ee); }
  .thumb-code { background: linear-gradient(135deg, #3f97a8, #a6dbe3); }

  .site-footer { position: absolute; left: 0; top: 701px; width: 1200px; height: 84px; background: var(--footer-bg); border-top: 3px solid var(--accent); }
  .footer-brand { position: absolute; left: 160px; top: 58px; width: 76px; text-align: center; font-size: 9px; color: #cfcfcf; white-space: nowrap; }
  .footer-info { position: absolute; left: 241px; top: 15px; height: 56px; border-left: 1px solid #777; padding-left: 9px; font-family: "Arimo", sans-serif; font-size: 12px; line-height: 19.5px; color: var(--footer-text); letter-spacing: 0.6px; }
  .footer-info .phone { color: var(--accent); }
  .footer-links { position: absolute; left: 915px; top: 14px; font-family: "Arimo", sans-serif; font-size: 12px; color: var(--footer-text); letter-spacing: 0.6px; }
  .footer-links span { margin: 0 10px; }
</style>
</head>
<body>
  <header class="site-header">
    <div class="brand">codeharborworks</div>
    <div class="search">
      <span class="search-label">Search</span>
      <svg class="search-icon" viewBox="0 0 34 23" aria-hidden="true">
        <circle cx="16" cy="10.5" r="5" fill="none" stroke="#666" stroke-width="2"/>
        <line x1="19.5" y1="14" x2="23" y2="17.5" stroke="#666" stroke-width="2.5" stroke-linecap="round"/>
      </svg>
    </div>
    <nav class="main-nav">
      <a class="is-current" href="#">home</a>
      <a href="#">web development</a>
      <a href="#">social media</a>
      <a href="#">server management</a>
      <a href="#">cloud deplyment</a>
      <a href="#">code review</a>
    </nav>
  </header>

  <section class="hero">
    <h2 class="hero-title">IS YOUR <span class="code-word">‹CODER›</span> SECURE?</h2>
    <p class="hero-line one">Do you know what a SQL Injection is<b>?</b></p>
    <p class="hero-line two">If you don’t know, that’s fine.</p>
    <p class="hero-cta-word">WE DO!</p>
    <div class="hero-button">Contact us and let’d Get Started
      <svg width="15" height="15" viewBox="0 0 15 15" aria-hidden="true">
        <circle cx="7.5" cy="7.5" r="7" fill="#5a1f1f"/>
        <path d="M6 4.5 L10 7.5 L6 10.5 Z" fill="#fff"/>
      </svg>
    </div>
    <div class="hero-art" role="img" aria-label="Cartoon developer holding a laptop and a pencil"></div>
    <div class="slider-dots"><span></span><span></span><span></span></div>
  </section>

  <main class="welcome">
    <h1>Welcome to <span>CodeHarborWorks</span></h1>
    <p>CodeHarborWorks, a team of 1 that can expand to 100 people in 5 seconds flat.</p>
    <p>CodeHarborWorks is elastic and extensible, providing our customers with all the necessary resources to complete their requirements on budget and on time.</p>
    <p>Click on one of our core competencies above to get an idea of what we do really, really well, day in and day out.</p>
  </main>

  <section class="services">
    <div class="service"><div class="service-thumb thumb-web" role="img" aria-label="WWW letters with tools"></div><div class="service-label"><b>Web</b> Development</div></div>
    <div class="service"><div class="service-thumb thumb-social" role="img" aria-label="Network of connected people figures"></div><div class="service-label"><b>Social</b> Media</div></div>
    <div class="service"><div class="service-thumb thumb-server" role="img" aria-label="Rows of server racks"></div><div class="service-label"><b>Server</b> Management</div></div>
    <div class="service"><div class="service-thumb thumb-cloud" role="img" aria-label="Computers linked around a globe"></div><div class="service-label"><b>Cloud</b> Deployment</div></div>
    <div class="service"><div class="service-thumb thumb-code" role="img" aria-label="Close-up of source code on a screen"></div><div class="service-label"><b>Code</b> Review</div></div>
  </section>

  <footer class="site-footer">
    <div class="footer-brand">codeharborworks</div>
    <div class="footer-info">
      Copyright © 2009-2012 CodeHarborWorks Inc.<br>
      Address: CodeHarborWorks, Inc. 41 Millbrook Lane Riverton, ON, K2P 7R4<br>
      Telephone: <span class="phone">+1 (555) 014-2290</span>
    </div>
    <div class="footer-links">Contact Us<span>|</span>Blog</div>
  </footer>
</body>
</html>
```